Flyer for Addiction program

Hi There,There are two parts to this project.1. A double-sided flyer for my next 5-day treatment program for addictions and family trauma.2. A one-page cover for the front of the course folders to match the above flyer?I have put together an information folder. Here is the filecrate link;https://www.filecrate.com/sh/jn7lkly6wcqphpt/AACmad0pag08NeuT2pM27USPa?dl=0Included in the information folder is;1. Copy2. Selection of images3. Logos and Brand identity kit4. Examples of past flyers and folder coverPlease don't hesitate to contact me if you have any questions.RegardsRebecca

Colors

Designer to choose colors to be used in the design.

Requirements
Must have
• 2 pages flyer please.
• Contemporary / fresh design

```html
<!DOCTYPE html>
<html lang="en">
<head>
<meta charset="utf-8">
<title>Breaking the Family Trance – 5 Day Program Flyer</title>
<link href="https://fonts.googleapis.com/css2?family=Montserrat:wght@400;500;600;700;800&display=swap" rel="stylesheet">
<style>
  :root{
    --navy:#14233a;
    --navy-deep:#0f1b2e;
    --ink:#1c2a40;
    --grey:#8a8682;
    --muted:#8b9bb0;
    --paper:#ffffff;
    --row:#f1f2f4;
    --stage:#e8e5e1;
  }
  *{box-sizing:border-box;margin:0;padding:0}
  html,body{width:1200px;height:903px;overflow:hidden;background:var(--stage);font-family:"Montserrat",Arial,sans-serif;color:var(--ink)}
  .canvas{position:relative;width:1200px;height:903px}
  .flyer{position:absolute;top:90px;width:510px;height:722px;background:var(--navy);overflow:hidden;box-shadow:0 4px 14px rgba(0,0,0,.25)}
  .flyer--front{left:58px}
  .flyer--back{left:623px}

  /* FRONT */
  .hero-photo{position:absolute;left:0;top:0;width:214px;height:722px;
    background:linear-gradient(180deg,#6b4a3a 0%,#8c4f3c 25%,#5a4a42 50%,#3a3a3c 70%,#1e2430 100%)}
  .front-panel{position:absolute;left:214px;top:0;width:296px;height:684px;background:var(--paper);
    border-bottom-left-radius:34px;padding:22px 20px 0 18px}
  .brand{text-align:center}
  .brand-dot{width:34px;height:34px;border-radius:50%;background:var(--grey);margin:0 auto 14px}
  .brand-name{font-size:11px;font-weight:500;letter-spacing:3px;color:var(--ink)}
  .title{text-align:center;margin-top:10px;line-height:.98}
  .title-line{display:block;font-weight:800;color:var(--navy)}
  .title-line--a{font-size:38px;letter-spacing:1px}
  .title-line--b{font-size:31px;color:var(--grey);letter-spacing:.5px}
  .title-line--c{font-size:45px;letter-spacing:1px}
  .title-sub{display:block;font-size:22px;font-weight:500;letter-spacing:1px;margin-top:4px}
  .quote{position:relative;margin:24px 2px 0;border:1.5px solid var(--navy);border-radius:10px;padding:12px 10px 10px;font-size:8px;line-height:1.3}
  .quote-mark{position:absolute;font-weight:800;font-size:22px;line-height:1;background:var(--paper);padding:0 2px;color:var(--navy)}
  .quote-mark--open{top:-12px;left:12px}
  .quote-mark--close{bottom:-14px;right:12px}
  .quote-author{text-align:right;margin-top:6px;margin-right:8px}
  .body{font-size:7.4px;line-height:1.27;text-align:justify;margin-top:14px}
  .body p+p{margin-top:8px}
  .section-head{font-size:8.4px;font-weight:700;margin-top:14px}
  .section-lead{font-size:8.2px;margin-top:2px}
  .checklist{list-style:none;margin-top:8px}
  .checklist li{position:relative;padding-left:12px;font-size:7.3px;line-height:1.25;margin-bottom:6px}
  .checklist li::before{content:"";position:absolute;left:1px;top:2px;width:5px;height:5px;border-radius:50%;background:var(--grey)}
  .front-email{position:absolute;left:214px;bottom:12px;width:296px;text-align:center;color:#fff;font-size:11px;letter-spacing:1.2px}

  /* BACK */
  .back-col{position:absolute;left:0;top:0;width:253px;height:722px;padding:18px 14px 0 22px;color:#fff}
  .back-lead-head{font-size:8.1px;font-weight:700;white-space:nowrap}
  .back-text{font-size:7.4px;line-height:1.25;text-align:justify;margin-top:8px}
  .benefits-head{font-size:8.2px;font-weight:700;margin-top:26px}
  .benefits-lead{font-size:8.2px;margin-top:2px}
  .benefits{list-style:none;margin-top:10px}
  .benefits li{position:relative;padding-left:10px;font-size:7.3px;line-height:1.25;text-align:justify;margin-bottom:9px}
  .benefits li::before{content:"";position:absolute;left:0;top:2px;width:4px;height:4px;border-radius:50%;background:#c6ccd6}
  .back-closing{font-size:7.4px;line-height:1.25;text-align:justify;margin-top:30px}
  .back-brand{text-align:center;margin-top:44px}
  .back-brand .brand-dot{background:#b9bcc0;margin-bottom:16px}
  .back-brand .brand-name{color:#fff;font-size:12px;letter-spacing:3.5px}
  .contact{margin-top:28px;font-size:9.8px;line-height:1.3}
  .contact-company{font-weight:700;color:var(--muted);margin-bottom:6px}
  .contact-label{font-weight:700}
  .contact p+p{margin-top:4px}
  .contact-email{white-space:nowrap}

  .back-side{position:absolute;left:253px;top:0;width:257px;height:390px;background:var(--paper);padding:16px 12px 0 12px;overflow:hidden}
  .details{width:100%;border-collapse:collapse;font-size:7.8px}
  .details caption{background:var(--navy);color:#fff;font-weight:600;font-size:7.8px;padding:3px 0;letter-spacing:.3px}
  .details td{padding:2px 5px;border-bottom:1px solid #fff;white-space:nowrap}
  .details tr:nth-child(odd) td{background:var(--row)}
  .side-head{font-size:10px;font-weight:600;letter-spacing:.4px;margin-top:12px}
  .side-text{font-size:7px;line-height:1.25;margin-top:5px}
  .investment{margin-top:14px;font-size:10px;font-weight:600;letter-spacing:.3px}
  .investment strong{font-size:14.5px;font-weight:700}
  .investment small{font-size:7.6px;font-weight:600}
  .family-photo{position:absolute;left:253px;top:390px;width:257px;height:294px;border-bottom-left-radius:34px;
    background:linear-gradient(180deg,#f2ede4 0%,#d9c79a 40%,#b48a3e 68%,#2a2418 88%,#14110c 100%)}
</style>
</head>
<body>
<main class="canvas">

  <section class="flyer flyer--front">
    <div class="hero-photo" role="img" aria-label="Hooded young man leaning against a red brick wall in a lane, reflected in a puddle"></div>
    <div class="front-panel">
      <div class="brand">
        <div class="brand-dot"></div>
        <div class="brand-name">HALCYON GROUP</div>
      </div>
      <h1 class="title">
        <span class="title-line title-line--a">BREAKING</span>
        <span class="title-line title-line--b">THE FAMILY</span>
        <span class="title-line title-line--c">TRANCE</span>
        <span class="title-sub">5 DAY PROGRAM</span>
      </h1>
      <blockquote class="quote">
        <span class="quote-mark quote-mark--open">“</span>
        If you cannot get rid of the family skeleton, you may as well make it dance
        <div class="quote-author">-Edmund Carraway</div>
        <span class="quote-mark quote-mark--close">”</span>
      </blockquote>
      <div class="body">
        <p>“Breaking the Family Trance” and breaking out of your adapted family roles is one of the most important things you can do to feel happy with yourself and in your relationships.</p>
        <p>Participating in Breaking the Family Trance will help you uncover the unconscious psychological defences, which create destructive habits and behaviour patterns that keep you stuck; recycling the same unfulfilling relationships, circumstances &amp; patterns in your life.</p>
      </div>
      <h2 class="section-head">HOW DO YOU KNOW IF YOU NEED TO BREAK FREE?</h2>
      <p class="section-lead">Consider the following questions:</p>
      <ul class="checklist">
        <li>Do you struggle to meet your own needs and wants, placing friends and family first?</li>
        <li>Do you adapt to fit in, be liked or accepted?</li>
        <li>Are you the one who is overly responsible for others or at work?</li>
        <li>Are you an over achiever only to find you are never satisfied with the end result?</li>
        <li>Do you suffer from repetitive, frustrating situations &amp; unhealthy behaviours in your personal and professional relationships?</li>
        <li>Are you “the one” who listens to others download their problems?</li>
        <li>Do you feel uncomfortable, asking others for help?</li>
        <li>Are you tired of being invisible?</li>
        <li>Do you find yourself feeling compelled to distract others, or use humour to ease emotional tension?</li>
        <li>Are you tired of searching for what you can DO or acquire to feel happy and satisfied?</li>
      </ul>
    </div>
    <div class="front-email">marjorie@thehalcyongroup.example</div>
  </section>

  <section class="flyer flyer--back">
    <div class="back-col">
      <h2 class="back-lead-head">Maybe it’s time to think about what you can undo!</h2>
      <p class="back-text">If you answered yes to any of the above questions, it’s likely that you are carrying a family legacy and a family role from your formative years that does not belong to you. If you seem to be sabotaging your success these roles and unconscious family patterns may very well be getting in the way of your happiness and well being.</p>
      <h3 class="benefits-head">PROGRAM BENEFITS</h3>
      <p class="benefits-lead">During the program you will learn how to:</p>
      <ul class="benefits">
        <li>Recognise the ways you adapt, so you can undo the false you and unleash the true you.</li>
        <li>Identify what you need to do for yourself to stop destructive behaviour patterns.</li>
        <li>Uncover important values that will bring you deep fulfilment.</li>
        <li>Speak up and be heard.</li>
        <li>Be present and be seen.</li>
        <li>Ask for help without feeling too embarrassed or vulnerable.</li>
        <li>Manage your emotions, rather than everyone else’s.</li>
        <li>Share responsibility with others and have more equal relationships.</li>
        <li>Discover what you really need and want, and learn the strategy of creating a vision</li>
        <li>Discover what your true needs are and work on getting them met.</li>
      </ul>
      <p class="back-closing">History doesn’t have to repeat itself! The program is specifically designed for those of you who are ready to address the CORE ISSUES that prevent you from experiencing success, freedom &amp; deep fulfilment in your relationships and in your life.</p>
      <div class="back-brand">
        <div class="brand-dot"></div>
        <div class="brand-name">HALCYON GROUP</div>
      </div>
      <div class="contact">
        <div class="contact-company">The Halcyon Group Pty Ltd.</div>
        <p>ABN 12 345 678 901 Wattle Crest Lane, Brookvale NSW 2700</p>
        <p><span class="contact-label">Phone:</span> 0400 555 019</p>
        <p class="contact-email"><span class="contact-label">Email:</span> marjorie@thehalcyongroup.example</p>
      </div>
    </div>

    <div class="back-side">
      <table class="details">
        <caption>PROGRAM DETAILS</caption>
        <tr><td>Thursday</td><td>24th January</td><td>9:00am - 5:00pm</td></tr>
        <tr><td>Friday</td><td>25th January</td><td>9:00am – 5:00pm</td></tr>
        <tr><td>Saturday</td><td>26th January</td><td>9:00am – 5:00pm</td></tr>
        <tr><td>Sunday</td><td>27th January</td><td>9:00am – 5:00pm</td></tr>
        <tr><td>Monday</td><td>28th October</td><td>9:00am – 5:00pm</td></tr>
      </table>
      <h3 class="side-head">ENROLMENT PROCESS</h3>
      <p class="side-text">Enrolments close Friday, 18th January 2019. To book your place, register your interest or find out more about this program please call Marjorie 0400 555 019.</p>
      <h3 class="side-head">INCLUSIONS</h3>
      <p class="side-text">A pre-program phone consult&nbsp; Relevant on online diagnostic survey’s<br>Integrated Equine Assisted Psychotherapy<br>Art Therapy Piece<br>All course materials (notebook, writing materials),<br>Morning and afternoon tea daily + light lunch</p>
      <p class="investment">INVESTMENTS : <strong>$2400</strong> <small>including GST</small></p>
      <h3 class="side-head">TERMS &amp; CONDITIONS</h3>
      <p class="side-text">A non-refundable deposit of $800 is required to hold your place.<br>Full payment is required by Friday 18th January 2019.<br>Premium card transactions incur a 3.3% merchant fee, standard cards 2.5%.<br>Direct debit facility available.</p>
    </div>
    <div class="family-photo" role="img" aria-label="Silhouette of a family at sunset, a parent lifting a child, another child on a bicycle with balloons"></div>
  </section>

</main>
</body>
</html>
```